Nutrition Supplements needs Logo and Package Design

We need logo and label design for the new nutrition and dietary supplement brand called "Fern Ledger".
It is a new brand for western world but is based on 150 year old formulations successfully sold in the East.

The first five formulations are slated to be launched in the US in November.
They will aid in conditions like:
1. Product One: Diabetes,
2. Product Two: Heart Health,
3. Product Three: Men's Health & Vitality,
4. Product Four: Women's Health and Menstrual conditions,
5. Product Five: Sport Nutrition Aid in keeping mind and body agile.

The competition will be Brightmeadow own brands and brands like Kelpstone Path.

All the five products will be packaged in HDPE bottle ( 1 bottle has 60 capsules )
Height / length : 94.5 mm
Width : 51 mm

Please feel free to ask any additional questions.

Reason: We are new to this website and modes of operation. We have added participation budget to the project from today. We are also launching a project on pixel harbor for website design tomorrow. This website will be for the same products for which this packaging design project is launched. We are excited to find good designers on this platform that we can work with in the long term

Target Market(s)

Females in the age group 30 - 75.
Aware of nutrition supplements and their benefits, the label will have to stand out when it's next to brands like Brightmeadow, Kelpstone path etc.. in the nutrition isle.
shop at stores like RVT, Brightmeadow, Internet, Merchant Olly's, Pantry Lane.

Industry/Entity Type

Nutrition

Requirements
Nice to have
• It would be nice to have logo design that vibrates combination of freshness, power of traditional remedies, age old secrets, and age defiance.

```html
<!DOCTYPE html>
<html lang="en">
<head>
<meta charset="utf-8">
<title>Fern Ledger – Diabetic Multivitamin Label</title>
<link rel="stylesheet" href="https://fonts.googleapis.com/css2?family=Bebas+Neue&family=Oswald:wght@600&display=swap">
<style>
  :root {
    --paper: #ffffff;
    --paper-tint: #eef4df;
    --leaf-green: #8cc63f;
    --leaf-green-deep: #7cb733;
    --band-edge: #a3d45a;
    --brand-brown: #7a4a2c;
    --title-white: #ffffff;
    --title-shade: #d9ddd6;
    --tab-text: #3b3a36;
    --produce-red: #c8402f;
    --produce-green: #5f9b3a;
    --produce-yellow: #e9c04a;
  }
  html, body {
    margin: 0;
    padding: 0;
    overflow: hidden;
    background: var(--paper);
  }
  .label {
    position: relative;
    width: 1200px;
    height: 2227px;
    overflow: hidden;
    background: linear-gradient(180deg, var(--paper) 0%, var(--paper) 12%, var(--paper-tint) 25%);
    font-family: "Bebas Neue", "Oswald", sans-serif;
  }
  .green-band {
    position: absolute;
    left: 0;
    top: 520px;
    width: 1200px;
    height: 1707px;
    display: block;
  }
  .brand {
    position: absolute;
    left: 0;
    top: 270px;
    width: 1200px;
    display: flex;
    justify-content: center;
    align-items: center;
    gap: 28px;
  }
  .brand-dot {
    width: 44px;
    height: 44px;
    border-radius: 50%;
    background: var(--leaf-green);
  }
  .brand-name {
    font-family: "Oswald", sans-serif;
    font-weight: 600;
    font-size: 118px;
    line-height: 1;
    color: var(--brand-brown);
    letter-spacing: 2px;
  }
  .product-title {
    position: absolute;
    left: 0;
    top: 690px;
    width: 1200px;
    margin: 0;
    text-align: center;
    color: var(--title-white);
    font-weight: 400;
    line-height: 0.86;
    text-shadow: 0 6px 10px rgba(40, 80, 10, 0.35);
  }
  .product-title .title-main {
    display: block;
    font-size: 348px;
    letter-spacing: 6px;
  }
  .product-title .title-sub {
    display: block;
    margin-top: 24px;
    font-size: 196px;
    letter-spacing: 5px;
  }
  .produce-basket {
    position: absolute;
    left: 94px;
    top: 1330px;
    width: 1068px;
    height: 620px;
    border-radius: 48% 48% 30% 30% / 40% 40% 22% 22%;
    background:
      radial-gradient(ellipse at 30% 65%, var(--produce-red) 0%, transparent 40%),
      radial-gradient(ellipse at 75% 70%, var(--produce-yellow) 0%, transparent 38%),
      radial-gradient(ellipse at 50% 40%, #a8733f 0%, transparent 55%),
      linear-gradient(180deg, var(--produce-green), #4d7f2c);
    opacity: 0.92;
  }
  .count-tab {
    position: absolute;
    left: 282px;
    top: 2078px;
    width: 636px;
    height: 170px;
    background: var(--paper);
    border-radius: 44px 44px 0 0;
    display: flex;
    justify-content: center;
    padding-top: 26px;
    box-sizing: border-box;
  }
  .count-tab span {
    font-family: "Oswald", sans-serif;
    font-weight: 600;
    font-size: 84px;
    line-height: 1;
    color: var(--tab-text);
    letter-spacing: 2px;
  }
</style>
</head>
<body>
  <main class="label">
    <svg class="green-band" viewBox="0 0 1200 1707" preserveAspectRatio="none" aria-hidden="true">
      <defs>
        <linearGradient id="bandFill" x1="0" y1="0" x2="0" y2="1">
          <stop offset="0" stop-color="#93cb47"/>
          <stop offset="1" stop-color="#7cb733"/>
        </linearGradient>
      </defs>
      <path d="M0 40 Q600 -20 1200 40 L1200 1707 L0 1707 Z" fill="url(#bandFill)"/>
      <path d="M0 40 Q600 -20 1200 40" fill="none" stroke="#b2dc70" stroke-width="6"/>
    </svg>

    <div class="brand">
      <span class="brand-dot"></span>
      <span class="brand-name">Fern Ledger</span>
    </div>

    <h1 class="product-title">
      <span class="title-main">DIABETIC</span>
      <span class="title-sub">MULTIVITAMIN</span>
    </h1>

    <div class="produce-basket" role="img" aria-label="Wicker basket filled with fresh vegetables and fruit: broccoli, peppers, corn, grapes, oranges, apples and bananas"></div>

    <div class="count-tab"><span>60 CAPSULES</span></div>
  </main>
</body>
</html>
```